Copper Lantern needs Stationary and Business Cards
Designs needs
Traditional
Delia R. Stroup
Owner
482 W. Hollin Creek Rd.
Harlow Bend, MI 49077
stroupd@lantern482.com
www.lantern482.com
What colors would you like? Black and Burnt Red
The Tavern will have an industrial chic style (updated vintage). I have attached a few clipart elements

```html
<!DOCTYPE html>
<html lang="en">
<head>
<meta charset="utf-8">
<title>Copper Lantern – Stationery Set</title>
<link rel="stylesheet" href="https://fonts.googleapis.com/css2?family=Open+Sans:wght@400;600&display=swap">
<style>
  :root {
    --backdrop: #8a7a73;
    --paper: #ffffff;
    --ink: #3a3535;
    --burnt-red: #a3382a;
    --fine-text: #4a4444;
    --edge: #d9d4d1;
  }
  * { box-sizing: border-box; margin: 0; padding: 0; }
  html, body { width: 1200px; height: 684px; overflow: hidden; }
  body {
    background: var(--backdrop);
    position: relative;
    font-family: "Open Sans", Arial, sans-serif;
    color: var(--fine-text);
  }
  .sheet {
    position: absolute;
    background: var(--paper);
    box-shadow: 0 1px 2px rgba(0,0,0,.18);
    border: 1px solid var(--edge);
    overflow: hidden;
  }
  .band {
    position: absolute;
    left: 0; right: 0; top: 0;
    background: var(--ink);
    border-bottom: 1.5px solid var(--burnt-red);
  }
  .brand {
    position: absolute;
    left: 0; right: 0;
    display: flex;
    align-items: center;
    justify-content: center;
    gap: .5em;
    font-weight: 600;
    letter-spacing: .06em;
    white-space: nowrap;
    color: var(--paper);
  }
  .brand-square {
    width: .6em;
    height: .6em;
    background: var(--burnt-red);
    flex: none;
  }
  .fine {
    position: absolute;
    left: 0; right: 0;
    text-align: center;
    font-size: 5px;
    line-height: 1.6;
    white-space: nowrap;
  }

  /* Letterhead */
  .letterhead { left: 240px; top: 43px; width: 356px; height: 600px; }
  .letterhead .band { height: 46px; }
  .letterhead .brand { top: 0; height: 46px; font-size: 13px; }
  .letterhead .fine { bottom: 14px; }

  /* Business card */
  .business-card { left: 34px; top: 307px; width: 202px; height: 113px; }
  .business-card .band { height: 19px; }
  .business-card .card-name {
    position: absolute; left: 0; right: 0; top: 6px;
    text-align: center; color: var(--paper);
    font-size: 5px; font-weight: 600; letter-spacing: .03em;
  }
  .business-card .brand { top: 42px; font-size: 10px; color: var(--ink); }
  .business-card .fine { bottom: 9px; font-size: 4.2px; }

  /* Envelope back */
  .envelope-back { left: 643px; top: 108px; width: 528px; height: 216px; }
  .envelope-back .band { height: 84px; }
  .envelope-back .brand { top: 0; height: 84px; font-size: 14px; }

  /* Envelope front */
  .envelope-front { left: 643px; top: 365px; width: 528px; height: 223px; }
  .envelope-front .band { height: 43px; }
  .envelope-front .brand { top: 0; height: 43px; font-size: 14px; }
  .envelope-front .fine { bottom: 14px; }
</style>
</head>
<body>

  <section class="sheet letterhead">
    <div class="band"></div>
    <p class="brand"><span class="brand-square"></span>COPPER LANTERN</p>
    <p class="fine">482 W. Hollin Creek Rd. Harlow Bend, MI 49077 &nbsp;|&nbsp; P: 555.010.0148 &nbsp;|&nbsp; E: stroupd@lantern482.com<br>www.lantern482.com</p>
  </section>

  <section class="sheet business-card">
    <div class="band"><p class="card-name">Delia R. Stroup &nbsp;|&nbsp; Owner</p></div>
    <p class="brand"><span class="brand-square"></span>COPPER LANTERN</p>
    <p class="fine">482 W. Hollin Creek Rd. Harlow Bend, MI 49077<br>P: 555.010.0148 &nbsp;|&nbsp; stroupd@lantern482.com &nbsp;|&nbsp; www.lantern482.com</p>
  </section>

  <section class="sheet envelope-back">
    <div class="band"></div>
    <p class="brand"><span class="brand-square"></span>COPPER LANTERN</p>
  </section>

  <section class="sheet envelope-front">
    <div class="band"></div>
    <p class="brand"><span class="brand-square"></span>COPPER LANTERN</p>
    <p class="fine">482 W. Hollin Creek Rd. Harlow Bend, MI 49077 &nbsp;|&nbsp; P: 555.010.0148 &nbsp;|&nbsp; E: stroupd@lantern482.com<br>www.lantern482.com</p>
  </section>

</body>
</html>
```